Keto Food Brand Needs Packaging Design and Logo

We need a logo and packaging design for a stand-up food bag for our keto shake mix. We are a health and wellness brand launching our first shake mix product. I would like bold, bright colors. This document goes more in depth . This brand might encompass more than only food so I want the logo to be versatile for supplements and other health products. https://files.quarnix-docs.example/share/8hTzq3PmVx41KdLw92RaYcbE07nGsJuQfM5oXt2iHkAp/view?mode=sharing See images of logos attached. It doesn't have to be food for the logo but I like the creativity of the ones listed.

Target Market(s)

Keto. Health and Fitness

Logo Text

Trevalo

Font styles to use
Serif
Sans Serif

Colors

Designer to choose colors to be used in the design.

```html
<!DOCTYPE html>
<html lang="en">
<head>
<meta charset="utf-8">
<title>Trevalo Strawberry Cheesecake Keto Shake Mix – Pouch Front</title>
<link rel="stylesheet" href="https://fonts.googleapis.com/css2?family=Fredoka:wght@400;600;700&display=swap">
<style>
  :root {
    --bg-deep: #4c0a2e;
    --bg-glow: #8a3461;
    --stripe-dark: #4a1f2c;
    --pouch-pink: #d8508c;
    --pouch-pink-light: #ec86b6;
    --pouch-rose: #b84a78;
    --label-silver: #e4e2ea;
    --label-shade: #c8c6d0;
    --ink-dark: #3f1a26;
    --title-blush: #f4cdd2;
    --badge-cream: #f6eef0;
    --band-purple: #9f4c88;
    --corner-light: #e9e6ee;
    --photo-cream: #e9dcc6;
    --photo-berry: #b8303e;
  }
  * { margin: 0; padding: 0; box-sizing: border-box; }
  html, body { width: 1200px; height: 800px; overflow: hidden; }
  body {
    background: radial-gradient(ellipse at 50% 28%, var(--bg-glow) 0%, #6a1a45 40%, var(--bg-deep) 85%);
    font-family: "Fredoka", sans-serif;
  }
  .pouch {
    position: absolute;
    left: 430px; top: 150px;
    width: 340px; height: 500px;
    overflow: hidden;
    background: linear-gradient(180deg, var(--pouch-pink) 0%, var(--pouch-pink-light) 55%, var(--pouch-rose) 100%);
  }
  .pouch-art { position: absolute; inset: 0; width: 340px; height: 500px; }
  .brand-label {
    position: absolute; left: 23px; top: 0;
    width: 133px; height: 222px;
    background: linear-gradient(180deg, var(--label-silver), var(--label-shade));
    display: flex; align-items: center; justify-content: center;
    padding-top: 56px;
  }
  .brand-name {
    font-weight: 400; font-size: 30px; color: var(--ink-dark);
    letter-spacing: 0.5px;
  }
  .claim-badge {
    position: absolute; left: 210px; top: 148px;
    width: 97px; height: 69px;
    border-radius: 48% 52% 46% 54% / 55% 50% 50% 45%;
    background: var(--badge-cream);
    display: flex; align-items: center; justify-content: center;
    text-align: center;
    font-size: 9.5px; line-height: 14px; color: var(--ink-dark);
    font-weight: 600;
  }
  .product-title {
    position: absolute; right: 24px; top: 228px;
    text-align: center; line-height: 1;
  }
  .flavour {
    display: block; font-weight: 700; font-size: 27px;
    color: var(--title-blush); letter-spacing: 0.3px;
  }
  .product-type {
    display: block; font-weight: 700; font-size: 18px;
    color: var(--ink-dark); margin-top: 2px;
  }
  .flavour-photo {
    position: absolute; left: 27px; top: 302px;
    width: 123px; height: 142px;
    border-radius: 40% 20% 45% 30%;
    background: radial-gradient(ellipse at 50% 45%, var(--photo-cream) 0 38%, var(--photo-berry) 72%, transparent 74%);
  }
  .feature {
    position: absolute; border-radius: 50%;
    display: flex; align-items: center; justify-content: center;
    text-align: center; font-weight: 700;
  }
  .feature-blend {
    left: 142px; top: 313px; width: 62px; height: 62px;
    background: var(--stripe-dark); color: var(--title-blush);
    font-size: 8.5px; line-height: 11px;
  }
  .feature-gluten {
    left: 190px; top: 340px; width: 60px; height: 60px;
    background: var(--badge-cream); color: var(--ink-dark);
    font-size: 12px; line-height: 16px;
  }
  .net-weight {
    position: absolute; left: 203px; top: 436px;
    width: 100px; text-align: center;
    transform: rotate(-45deg);
    font-size: 13px; font-weight: 400; color: var(--title-blush);
    letter-spacing: 0.5px;
  }
</style>
</head>
<body>
  <div class="pouch">
    <svg class="pouch-art" viewBox="0 0 340 500" aria-hidden="true">
      <g fill="var(--stripe-dark)">
        <rect x="0" y="0" width="340" height="27"/>
        <rect x="0" y="54" width="340" height="27"/>
        <rect x="0" y="108" width="340" height="27"/>
        <rect x="0" y="162" width="340" height="27"/>
      </g>
      <polygon points="340,280 340,500 105,500" fill="var(--stripe-dark)"/>
      <polygon points="340,360 340,500 184,500" fill="var(--band-purple)"/>
      <polygon points="340,443 340,500 267,500" fill="var(--corner-light)"/>
    </svg>

    <div class="brand-label">
      <span class="brand-name">Trevalo</span>
    </div>

    <div class="claim-badge">NO ARTIFICIAL<br>COLOURS OR<br>FLAVOURS</div>

    <h1 class="product-title">
      <span class="flavour">STRAWBERRY</span>
      <span class="flavour">CHEESECAKE</span>
      <span class="product-type">KETO SHAKE MIX</span>
    </h1>

    <div class="flavour-photo" role="img" aria-label="Photo of a slice of strawberry cheesecake topped with fresh strawberries and sauce"></div>

    <div class="feature feature-blend">BLENDS<br>SMOOTHLY</div>
    <div class="feature feature-gluten">GLUTEN<br>FREE</div>

    <div class="net-weight">NET WT 2 LB</div>
  </div>
</body>
</html>
```